Bride Basecamp

I am looking for a design for http://www.bridebasecamp.co.uk/ its a joomla site and I am going to set up with the same mods as our stag version http://www.groomnightout.co.uk/ you will see on groomnight how all the menus look and are positioned. Here is an example of a activity page http://www.groomnightout.co.uk/activity/white-water-rafting-in-perthshire.html which comes from Kiln.

The design needs to be built for responsive layout. The brand look and feel needs to be 100% for the female market.

We can accept the design in photoshop or something similar

Please ask questions if you require more information.

some examples of hen sites

http://www.maidenmerry.co.uk/

```html
<!DOCTYPE html>
<html lang="en">
<head>
<meta charset="utf-8">
<title>Bride Basecamp</title>
<link href="https://fonts.googleapis.com/css2?family=Oswald:wght@400;500&family=Open+Sans:wght@400;600;700&display=swap" rel="stylesheet">
<style>
:root{
  --green:#2a8c12;
  --green-bright:#3aa51c;
  --dark:#111;
  --header-bg:#1c1c1c;
  --footer-bg:#333;
  --text:#555;
  --heading:#333;
  --line:#ddd;
  --white:#fff;
  --star:#2a8c12;
}
*{box-sizing:border-box;margin:0;padding:0}
html,body{width:736px;height:1200px;overflow:hidden;background:var(--white);font-family:'Open Sans',sans-serif;color:var(--text)}
.page{position:relative;width:736px;height:1200px}
.abs{position:absolute}
.header{left:0;top:0;width:736px;height:342px;background:radial-gradient(ellipse at 50% 30%,#555 0%,#222 55%,#0d0d0d 100%)}
.brand{left:80px;top:16px;font-family:'Oswald',sans-serif;font-weight:500;font-size:21px;color:var(--green-bright);letter-spacing:.3px}
.social{left:366px;top:19px;display:flex;gap:7px}
.social span{width:17px;height:17px;border-radius:50%;background:#eee;display:block}
.search{left:510px;top:17px;width:133px;height:24px;background:var(--white);font-size:7px;color:#666;padding:7px 7px}
.search svg{position:absolute;right:8px;top:6px}
.nav{left:80px;top:57px;width:576px;height:35px;background:var(--green);display:flex;align-items:center;box-shadow:0 2px 4px rgba(0,0,0,.5)}
.nav a{font-size:10px;font-weight:600;color:var(--white);text-decoration:none;padding:0 16px}
.nav a.home{background:var(--dark);height:35px;line-height:35px;padding:0 23px 0 28px;margin-right:2px}
.slide{left:92px;top:96px;width:551px;height:218px;background:linear-gradient(120deg,#7a1810 0%,#c7443a 35%,#e6a48e 55%,#b3362b 75%,#5a0d08 100%)}
.slide-brand{left:110px;top:240px;font-family:'Oswald',sans-serif;font-size:26px;color:#ffe600;display:flex;align-items:center;gap:6px}
.slide-brand i{width:16px;height:16px;background:#ffe600;display:block}
.slide-caption{left:92px;top:297px;font-size:10px;color:var(--white);letter-spacing:.4px}
.slide-bar{left:92px;top:314px;width:551px;height:28px;background:#050505}
.dots{left:333px;top:324px;display:flex;gap:3px}
.dots span{width:7px;height:7px;border-radius:50%;background:var(--white);display:block}
.dots span.on{background:var(--green-bright)}
h2{font-family:'Oswald',sans-serif;font-weight:500;font-size:15px;color:var(--heading)}
h2 em{font-style:normal;color:var(--green)}
.welcome{left:95px;top:352px;font-size:17px}
.video{left:94px;top:385px;width:216px;height:157px;background:#222;border:1px solid #999}
.video-title{left:3px;top:2px;font-size:6px;color:#eee}
.video-screen{left:3px;top:12px;width:208px;height:128px;background:linear-gradient(#2548e0 0%,#2548e0 45%,#fff 45%)}
.video-screen .vb{left:8px;top:18px;font-family:'Oswald',sans-serif;font-size:20px;color:#ffe600}
.video-screen p{position:absolute;left:6px;font-size:6.5px;font-weight:700;color:#222;font-style:italic}
.play{left:87px;top:52px;width:38px;height:26px;border-radius:6px;background:rgba(20,20,20,.85)}
.video-controls{left:3px;top:142px;width:208px;height:12px;font-size:5px;color:#ddd;padding:3px 0 0 48px}
.intro{left:332px;top:386px;width:312px;font-size:6.6px;line-height:17.3px;color:#666}
.rule{height:1px;background:var(--line)}
.dotline{height:0;border-top:2px dotted var(--green)}
.card{width:311px;height:81px;border:1px solid var(--line);box-shadow:0 1px 2px rgba(0,0,0,.1)}
.photo{display:block}
.card .photo{position:absolute;left:3px;top:4px;width:82px;height:70px}
.card h3{position:absolute;left:108px;top:1px;font-family:'Oswald',sans-serif;font-weight:400;font-size:11px;color:#555}
.card p{position:absolute;left:108px;top:25px;width:200px;font-size:6.5px;line-height:12.5px;color:#666}
.meta{position:absolute;left:108px;top:58px;display:flex;align-items:center;gap:6px;font-size:5.5px;color:var(--green)}
.meta .clock{width:10px;height:10px;border-radius:50%;background:#aaa;margin-left:3px}
.btn{position:absolute;left:246px;top:52px;width:62px;height:21px;background:#ddd;font-size:6.5px;color:#555;text-align:center;line-height:21px}
.review{left:415px;width:228px}
.review .photo{position:absolute;left:0;top:0;width:73px;height:67px}
.review h4{position:absolute;left:101px;top:6px;font-family:'Oswald',sans-serif;font-weight:400;font-size:8px;color:#333}
.review p{position:absolute;left:101px;top:18px;width:128px;font-size:6.3px;line-height:15px;color:#666}
.review p b{font-weight:400;color:var(--green)}
.stars{position:absolute;left:101px;top:57px;display:flex;gap:1px}
.review .date{position:absolute;right:10px;top:58px;font-size:6.5px;color:var(--green)}
.grid{left:92px;top:926px;width:310px;height:153px;display:grid;grid-template-columns:repeat(4,1fr);grid-template-rows:repeat(2,1fr);gap:1px;background:var(--white)}
.note{left:418px;width:225px}
.note h5{font-size:7px;font-weight:700;color:var(--green)}
.note p{margin-top:6px;font-size:6.3px;line-height:13.5px;color:#666}
.footer{left:0;top:1092px;width:736px;height:108px;background:var(--footer-bg)}
.f-social{left:323px;top:1109px;display:flex;gap:5px}
.f-social span{width:19px;height:19px;border-radius:50%;background:#ddd;display:block}
.f-links{left:0;top:1142px;width:736px;text-align:center;font-size:6.8px;color:var(--white)}
.f-links span{margin:0 5px}
.copy{left:0;top:1169px;width:736px;text-align:center;font-size:6.5px;color:var(--white)}
</style>
</head>
<body>
<div class="page">
  <header class="header abs"></header>
  <div class="brand abs">BRIDE BASECAMP</div>
  <div class="social abs" aria-label="Social links"><span></span><span></span><span></span><span></span><span></span></div>
  <div class="search abs">Search
    <svg width="10" height="10" viewBox="0 0 10 10"><circle cx="4" cy="4" r="3" fill="none" stroke="#555" stroke-width="1.3"/><line x1="6.2" y1="6.2" x2="9.3" y2="9.3" stroke="#555" stroke-width="1.6"/></svg>
  </div>
  <nav class="nav abs">
    <a class="home">Home</a><a>About Us</a><a>Locations</a><a>Gallery</a><a>Events</a><a>News</a><a>Blog</a><a>Contact Us</a>
  </nav>
  <div class="slide abs photo" role="img" aria-label="Group of friends in festive hats celebrating with glasses of champagne"></div>
  <div class="slide-brand abs"><i></i>Zestival</div>
  <div class="slide-caption abs">"Part of the Zestival Network"</div>
  <div class="slide-bar abs"></div>
  <div class="dots abs"><span class="on"></span><span></span><span></span><span></span><span></span></div>

  <h2 class="welcome abs"><em>WELCOME TO</em> BRIDE BASECAMP</h2>
  <div class="video abs">
    <div class="video-title abs">Rory The Lime Explaining Our Zestival Party ...</div>
    <div class="video-screen abs">
      <div class="vb abs">Zestival</div>
      <p style="top:84px">Click to watch a very short video explaining what to do next and<br>how Zestival can help.</p>
      <p style="top:110px">We have some great FREE tools online to help manage groups</p>
      <div class="play abs"><svg width="38" height="26"><polygon points="16,8 16,18 24,13" fill="#fff"/></svg></div>
    </div>
    <div class="video-controls abs">0:00 / 1:20</div>
  </div>
  <p class="intro abs">Bride Basecamp is the place to start if you want to put together a great hen party. We have done 1000's of them over the years and know all the great places and things to do. Rather than build a big site with loads of pages that you will never read we decided lets cut to the chase and make it easy for you. chase and make it easy for you 1000's of them over the chase and make it easy for you.and make it easy for you. chase and make it easy for you 1000's of them over the chase and make it easy for you and make it easy for you.and make it easy for you. chase and make it easy for you 1000's and make it easy for you and make it easy for you.and make it easy for you. chase and make it easy for you 1000's .........</p>
  <div class="rule abs" style="left:92px;top:553px;width:551px"></div>

  <h2 class="abs" style="left:92px;top:561px"><em>Booking</em> Your Hen Do</h2>
  <div class="dotline abs" style="left:92px;top:587px;width:105px"></div>
  <div class="rule abs" style="left:197px;top:588px;width:203px;border-top:1px dotted #bbb;height:0;background:none"></div>
  <h2 class="abs" style="left:413px;top:561px"><em>Customer</em> Reviews</h2>
  <div class="dotline abs" style="left:415px;top:587px;width:228px;border-top-style:dotted;border-top-color:#bbb;border-top-width:1px"></div>

  <div class="card abs" style="left:92px;top:598px">
    <div class="photo" role="img" aria-label="Woman dancing under warm club lights" style="background:linear-gradient(135deg,#3a1208,#c8502a,#f0a060)"></div>
    <h3>Night Lumina Party</h3>
    <p>We have loads of customers using our services time and time again. We pride ourselves on delivering....</p>
    <div class="meta"><svg width="7" height="9" viewBox="0 0 7 9"><path d="M3.5 0A3.3 3.3 0 0 0 .2 3.3C.2 5.6 3.5 9 3.5 9s3.3-3.4 3.3-5.7A3.3 3.3 0 0 0 3.5 0z" fill="#aaa"/></svg>Velvet Glow Club<span class="clock"></span>All Day</div>
    <div class="btn">BUY TICKETS</div>
  </div>
  <div class="card abs" style="left:92px;top:688px">
    <div class="photo" role="img" aria-label="Crowd dancing under blue stage lights" style="background:linear-gradient(160deg,#0a1a5a,#2a5ad0,#101030)"></div>
    <h3>Night Lumina Party</h3>
    <p>We have loads of customers using our services time and time again. We pride ourselves on delivering....</p>
    <div class="meta"><svg width="7" height="9" viewBox="0 0 7 9"><path d="M3.5 0A3.3 3.3 0 0 0 .2 3.3C.2 5.6 3.5 9 3.5 9s3.3-3.4 3.3-5.7A3.3 3.3 0 0 0 3.5 0z" fill="#aaa"/></svg>Velvet Glow Club<span class="clock"></span>All Day</div>
    <div class="btn">BUY TICKETS</div>
  </div>
  <div class="card abs" style="left:92px;top:777px">
    <div class="photo" role="img" aria-label="Friends celebrating on a purple lit dance floor" style="background:linear-gradient(135deg,#3a0a5a,#a040c0,#e0b0d0)"></div>
    <h3>Night Lumina Party</h3>
    <p>We have loads of customers using our services time and time again. We pride ourselves on delivering....</p>
    <div class="meta"><svg width="7" height="9" viewBox="0 0 7 9"><path d="M3.5 0A3.3 3.3 0 0 0 .2 3.3C.2 5.6 3.5 9 3.5 9s3.3-3.4 3.3-5.7A3.3 3.3 0 0 0 3.5 0z" fill="#aaa"/></svg>Velvet Glow Club<span class="clock"></span>All Day</div>
    <div class="btn">BUY TICKETS</div>
  </div>

  <div class="review abs" style="top:600px;height:80px">
    <div class="photo" role="img" aria-label="Women dancing at a party with red lights" style="background:linear-gradient(135deg,#6a0a20,#d04060,#f0c0a0)"></div>
    <h4>EXCELLENT!!!!!!!!!!!!!!!!!!!!!!!!!!!!!</h4>
    <p>Bride Basecamp is the place to start if you put together a great party....<b>READ MORE</b></p>
    <div class="stars"><svg width="48" height="8" viewBox="0 0 48 8"><g fill="#2a8c12"><polygon points="4,0 5,3 8,3 5.5,5 6.5,8 4,6 1.5,8 2.5,5 0,3 3,3"/><polygon transform="translate(10 0)" points="4,0 5,3 8,3 5.5,5 6.5,8 4,6 1.5,8 2.5,5 0,3 3,3"/><polygon transform="translate(20 0)" points="4,0 5,3 8,3 5.5,5 6.5,8 4,6 1.5,8 2.5,5 0,3 3,3"/><polygon transform="translate(30 0)" points="4,0 5,3 8,3 5.5,5 6.5,8 4,6 1.5,8 2.5,5 0,3 3,3"/></g><polygon transform="translate(40 0)" fill="#777" points="4,0 5,3 8,3 5.5,5 6.5,8 4,6 1.5,8 2.5,5 0,3 3,3"/></svg></div>
  </div>
  <div class="rule abs" style="left:415px;top:679px;width:228px"></div>
  <div class="review abs" style="top:689px;height:80px">
    <div class="photo" role="img" aria-label="Women celebrating at a bar" style="background:linear-gradient(135deg,#3a0a0a,#a02818,#e07040)"></div>
    <h4>EXCELLENT!!!!!!!!!!!!!!!!!!!!!!!!!!!!!</h4>
    <p>Bride Basecamp is the place to start if you put together a great party.... <b>READ MORE</b></p>
    <div class="stars"><svg width="48" height="8" viewBox="0 0 48 8"><g fill="#2a8c12"><polygon points="4,0 5,3 8,3 5.5,5 6.5,8 4,6 1.5,8 2.5,5 0,3 3,3"/><polygon transform="translate(10 0)" points="4,0 5,3 8,3 5.5,5 6.5,8 4,6 1.5,8 2.5,5 0,3 3,3"/><polygon transform="translate(20 0)" points="4,0 5,3 8,3 5.5,5 6.5,8 4,6 1.5,8 2.5,5 0,3 3,3"/><polygon transform="translate(30 0)" points="4,0 5,3 8,3 5.5,5 6.5,8 4,6 1.5,8 2.5,5 0,3 3,3"/></g><polygon transform="translate(40 0)" fill="#777" points="4,0 5,3 8,3 5.5,5 6.5,8 4,6 1.5,8 2.5,5 0,3 3,3"/></svg></div>
    <span class="date">12,Jan 2014</span>
  </div>
  <div class="rule abs" style="left:415px;top:768px;width:228px"></div>
  <div class="review abs" style="top:778px;height:80px">
    <div class="photo" role="img" aria-label="Three friends posing together at a night out" style="background:linear-gradient(135deg,#2a0a5a,#8040c0,#d0a0b0)"></div>
    <h4>EXCELLENT!!!!!!!!!!!!!!!!!!!!!!!!!!!!!</h4>
    <p>Bride Basecamp is the place to start if you put together a great party....<b>READ MORE</b></p>
    <div class="stars"><svg width="48" height="8" viewBox="0 0 48 8"><g fill="#2a8c12"><polygon points="4,0 5,3 8,3 5.5,5 6.5,8 4,6 1.5,8 2.5,5 0,3 3,3"/><polygon transform="translate(10 0)" points="4,0 5,3 8,3 5.5,5 6.5,8 4,6 1.5,8 2.5,5 0,3 3,3"/><polygon transform="translate(20 0)" points="4,0 5,3 8,3 5.5,5 6.5,8 4,6 1.5,8 2.5,5 0,3 3,3"/><polygon transform="translate(30 0)" points="4,0 5,3 8,3 5.5,5 6.5,8 4,6 1.5,8 2.5,5 0,3 3,3"/></g><polygon transform="translate(40 0)" fill="#777" points="4,0 5,3 8,3 5.5,5 6.5,8 4,6 1.5,8 2.5,5 0,3 3,3"/></svg></div>
    <span class="date">12,Jan 2014</span>
  </div>
  <div class="rule abs" style="left:415px;top:857px;width:228px"></div>

  <div class="rule abs" style="left:92px;top:880px;width:551px"></div>
  <h2 class="abs" style="left:93px;top:888px"><em>LATEST</em> BLOG</h2>
  <div class="dotline abs" style="left:92px;top:914px;width:85px"></div>
  <div class="abs" style="left:177px;top:915px;width:225px;border-top:1px dotted #bbb"></div>
  <div class="grid abs">
    <div class="photo" role="img" aria-label="Friends posing together" style="background:linear-gradient(135deg,#6a4a3a,#c09070)"></div>
    <div class="photo" role="img" aria-label="Party crowd in a bar" style="background:linear-gradient(135deg,#3a2a1a,#8a6040)"></div>
    <div class="photo" role="img" aria-label="Women on a blue lit dance floor" style="background:linear-gradient(135deg,#101a5a,#4a60b0)"></div>
    <div class="photo" role="img" aria-label="Woman laughing under bright lights" style="background:linear-gradient(135deg,#8a6a5a,#e0c0a0)"></div>
    <div class="photo" role="img" aria-label="Friends in pink outfits" style="background:linear-gradient(135deg,#a02040,#e08080)"></div>
    <div class="photo" role="img" aria-label="Guest relaxing in a dim lounge" style="background:linear-gradient(135deg,#2a2a2a,#7a7060)"></div>
    <div class="photo" role="img" aria-label="Group dancing at a club night" style="background:linear-gradient(135deg,#1a1a3a,#6a5a8a)"></div>
    <div class="photo" role="img" aria-label="Friends grouped for a night out photo" style="background:linear-gradient(135deg,#2a3a5a,#b0a090)"></div>
  </div>

  <h2 class="abs" style="left:415px;top:888px"><em>Great</em> Reviews</h2>
  <div class="dotline abs" style="left:415px;top:914px;width:233px;border-top-style:dotted;border-top-color:#bbb;border-top-width:1px"></div>
  <div class="note abs" style="top:925px">
    <h5>[12 JAN 2014]</h5>
    <p>We have made it really simple. For a deposit of only £10 per person, we reserve and book your whole hen party including the accommo-dation!.</p>
  </div>
  <div class="rule abs" style="left:415px;top:992px;width:228px"></div>
  <div class="note abs" style="top:1001px">
    <h5>[12 JAN 2014]</h5>
    <p>We have made it really simple. For a deposit of only £10 per person, we reserve and book your whole hen party including the accommo-dation!.</p>
  </div>
  <div class="rule abs" style="left:415px;top:1068px;width:228px"></div>

  <footer class="footer abs"></footer>
  <div class="f-social abs" aria-label="Social links"><span></span><span></span><span></span><span></span></div>
  <div class="f-links abs">Home<span>/</span>About Us<span>/</span>Locations<span>/</span>Gallery<span>/</span>Events News<span>/</span>Blog<span>/</span>Contact Us</div>
  <div class="copy abs">Copyright 2014 Bride Basecamp.All Right Reseved.</div>
</div>
</body>
</html>
```